Kovela" is new brand of luxury olive oil. We need logo, bottle design and corporate stationary created.

We would like to more focus on the logo and bottle design. I have attached the specification for bottles that will have print on them.

The term “Kovela” is specific for the Mediteran region of Priimošten and it represents the parts of the former vineyards of Well known Babić vine, which were literally planted in scarce, Rocky soil. Today, the days of vineyards are far behind us. Vine was long ago replaced with Olive groves on that same, scarce, Rocky soil. Primošten is also Well known for its dry climate which was described long time ago, dating back in Roman ages. Scarce, Rocky soil and dry climate enable the production of healthy Olive fruits with the unique taste, aroma and texture. ALL of our olive groves are maintained only by donkeys, the forgotten symbol of Primošten, The man’s best friend for hundreds of Years in the region of Dalmatia, enabling the 100 % ecological production of olives and preservation of tradition, which we are very proud of. Since ours Olive groves Are placed only on hilly, inaccessible terrain, carved in stones, picking olives can be done only by hand, resulting in the best quality.

We will print our package design on bottles:
- 0,1l small bottles that will used as gifts
- 0,5l bottles
- 0,75 l bottles
Send us ideas with bottles that can used for our brand and please send us link where we can order them and stay in 1 $ max per bottle range.

Here are some brands that we like. Logo and packaging:
- https://www.pelu5-8.com/en/
- https://www.grandevik.com/en/producto/vk-shop-extra-virgin-olive-oil-organic-premium-500-ml-box/
- https://plazquorstudio.com/branding-and-packaging-for-greek-extra-virgin-olive-oil/

```html
<!DOCTYPE html>
<html lang="en">
<head>
<meta charset="utf-8">
<title>Kovela Extra Virgin Olive Oil — Bottle Design</title>
<link rel="stylesheet" href="https://fonts.googleapis.com/css2?family=Cinzel:wght@500&family=Montserrat:wght@400;600&display=swap">
<style>
  :root {
    --backdrop: #f4f4f4;
    --glass: #0c0c0c;
    --cap: #1a1a1a;
    --gold: #c9a45c;
    --emblem-tone: #1c1812;
  }
  html, body {
    margin: 0;
    padding: 0;
    width: 859px;
    height: 1200px;
    overflow: hidden;
    background: var(--backdrop);
  }
  .bottle-range {
    display: block;
    width: 859px;
    height: 1200px;
  }
  .glass { fill: var(--glass); }
  .cap { fill: var(--cap); }
  .cap-ridge { stroke: #2a2a2a; stroke-width: 1; }
  .brand-name {
    font-family: "Cinzel", serif;
    font-weight: 500;
    fill: var(--gold);
    text-anchor: middle;
    letter-spacing: 1px;
  }
  .emblem-area { fill: url(#emblemTone); }
  .label-text {
    font-family: "Montserrat", sans-serif;
    fill: var(--gold);
    text-anchor: middle;
  }
  .product-type { font-weight: 400; letter-spacing: 2.4px; }
  .product-name { font-weight: 600; letter-spacing: 2.4px; }
  .origin { font-weight: 400; letter-spacing: 1.4px; }
  .volume { font-weight: 400; }
  .separator { fill: var(--gold); }
</style>
</head>
<body>
<svg class="bottle-range" viewBox="0 0 859 1200" xmlns="http://www.w3.org/2000/svg">
  <defs>
    <linearGradient id="emblemTone" x1="0" y1="0" x2="0" y2="1">
      <stop offset="0" stop-color="var(--emblem-tone)" stop-opacity="0.4"/>
      <stop offset="1" stop-color="var(--emblem-tone)" stop-opacity="1"/>
    </linearGradient>
  </defs>

  <!-- 500 ml bottle -->
  <g class="bottle bottle-500">
    <rect class="glass" x="210" y="500" width="98" height="130"/>
    <rect class="glass" x="105" y="622" width="310" height="494" rx="16"/>
    <rect class="cap" x="204" y="456" width="109" height="50" rx="4"/>
    <g class="cap-ridge">
      <line x1="204" y1="466" x2="313" y2="466"/>
      <line x1="204" y1="476" x2="313" y2="476"/>
      <line x1="204" y1="486" x2="313" y2="486"/>
      <line x1="204" y1="496" x2="313" y2="496"/>
    </g>

    <text class="brand-name" x="260" y="716" font-size="38">KOVELA</text>

    <rect class="emblem-area" x="240" y="801" width="40" height="148" rx="4"
          role="img" aria-label="Gold drip emblem of the brand"/>

    <text class="label-text product-type" x="260" y="1017" font-size="13">EXTRA VIRGIN</text>
    <text class="label-text product-name" x="260" y="1033" font-size="13">OLIVE OIL</text>
    <text class="label-text origin" x="260" y="1050" font-size="9.5">MADE IN PRIMOŠTEN</text>
    <circle class="separator" cx="260" cy="1062" r="1.3"/>
    <text class="label-text volume" x="260" y="1083" font-size="11">500ml</text>
  </g>

  <!-- 750 ml bottle -->
  <g class="bottle bottle-750">
    <rect class="glass" x="522" y="128" width="106" height="220"/>
    <path class="glass" d="M522,340 C522,385 447,388 447,435 L447,1104 Q447,1120 463,1120 L689,1120 Q705,1120 705,1104 L705,435 C705,388 628,385 628,340 Z"/>
    <rect class="cap" x="520" y="65" width="110" height="72" rx="5"/>
    <g class="cap-ridge">
      <line x1="520" y1="78" x2="630" y2="78"/>
      <line x1="520" y1="90" x2="630" y2="90"/>
      <line x1="520" y1="102" x2="630" y2="102"/>
      <line x1="520" y1="114" x2="630" y2="114"/>
      <line x1="520" y1="126" x2="630" y2="126"/>
    </g>

    <text class="brand-name" x="576" y="504" font-size="39">KOVELA</text>

    <rect class="emblem-area" x="552" y="637" width="48" height="257" rx="4"
          role="img" aria-label="Gold drip emblem of the brand"/>

    <text class="label-text product-type" x="576" y="999" font-size="13">EXTRA VIRGIN</text>
    <text class="label-text product-name" x="576" y="1015" font-size="13">OLIVE OIL</text>
    <text class="label-text origin" x="576" y="1031" font-size="9.5">MADE IN PRIMOŠTEN</text>
    <circle class="separator" cx="576" cy="1044" r="1.3"/>
    <text class="label-text volume" x="576" y="1065" font-size="11">750ml</text>
  </g>

</svg>
</body>
</html>
```